VexaQuor - Risk Analysis Software For the Petroleum Professional

We are a small niche software engineering firm delivering innovative software products for the Energy Industry and have been in business since 2002. For the immediate task I am looking for a professional landing page for one of our software products (VexaQuorĀ®) that will attract new clients and promote sales leads.
Secondarily (as a follow up) I am also looking for a new website design. The current website we have is very outdated so I am also looking for the landing page design to feed into a contemporary web site with a similar design as the landing page. Maybe I am going about this backwards? I will look for your recommendations. I estimate 4 to 5 pages are needed for the new website, one will contain a form for collecting client inquiries. Here is a link to a form that I have used in the past.
https://www.vexaquor-demo.net/request1.html
The form should append new records to a database and generate an email to the client for acknowledgement and finish with a confirmation page or equivalent effect.
Our current provider is Pellway Hosting (or Hostrix.example).
https://www.vexaquor-demo.net/
I have many JPG images of screen shots and presentation images and I want to be able to circulate these images on my end after the page has been constructed. So (when possible) the images that are used within the page(s) need to be referenced individually.
The web page(s) need to be view compatible on all devices. Windows, Mac, ios iPhone and iPad and Android.
VexaQuorĀ® is a US registered trademark.
Uploaded is a short PowerPoint Slide presentation.
Note: The company that owns this software is my company called VexaQuor, LLC
Updates
Confirming....This project is for a landing page design with its HTML/CSS files and referenced images.
Target Market(s)
Oil Companies
Industry/Entity Type
Energy
Colors
Designer to choose colors to be used in the design.
Look and feel

```html
<!DOCTYPE html>
<html lang="en">
<head>
<meta charset="utf-8">
<title>VexaQuor – Risk Analysis Software for the Petroleum Professional</title>
<link href="https://fonts.googleapis.com/css2?family=Montserrat:ital,wght@0,400;0,500;0,600;0,700;0,800;1,400&display=swap" rel="stylesheet">
<style>
:root{
  --red:#e30613;
  --red-deep:#8c0508;
  --red-dark:#4a0204;
  --black:#050505;
  --ink:#1b1b1b;
  --text:#4a4a4a;
  --muted:#8a8a8a;
  --line:#c9c9c9;
  --grey-bg:#efefef;
  --footer:#1e1e1e;
  --white:#ffffff;
}
*{box-sizing:border-box;margin:0;padding:0}
html,body{width:1200px;height:3797px;overflow:hidden}
body{font-family:"Montserrat",Arial,sans-serif;color:var(--text);background:var(--white);position:relative}
section,header,footer{position:absolute;left:0;width:1200px;overflow:hidden}
.abs{position:absolute}
.center{text-align:center;left:0;width:1200px}
.brand{font-family:"Montserrat",Arial,sans-serif;font-weight:800;letter-spacing:-1px}
.brand sup{font-size:.4em;font-weight:800;vertical-align:top;position:relative;top:.2em}
.section-title{font-size:30px;font-weight:700;color:var(--ink);letter-spacing:.5px}
.section-title span{color:var(--red)}
.title-rule{width:60px;height:3px;background:var(--red);left:570px}

/* header */
.site-header{top:0;height:70px;background:var(--black)}
.site-header .logo{left:130px;top:10px;font-size:40px;color:var(--red)}
.main-nav a{position:absolute;top:26px;font-size:12px;color:#e6e6e6;text-decoration:none;letter-spacing:.3px}
.main-nav a.active{font-weight:700;color:var(--white)}

/* hero */
.hero{top:70px;height:624px;background:
  radial-gradient(ellipse at 70% 70%,#b10a10 0%,transparent 55%),
  radial-gradient(ellipse at 30% 30%,#7a0a0c 0%,transparent 60%),
  linear-gradient(90deg,#1a0405 0%,#5a0507 25%,#a00a0e 60%,#d4141a 100%)}
.hero-photo{left:0;top:0;width:1200px;height:624px}
.hero .brand{top:140px;font-size:72px;color:var(--white)}
.hero h1{top:240px;font-size:32px;font-weight:600;color:var(--white);line-height:37px;letter-spacing:.5px}
.hero p{top:322px;left:225px;width:750px;font-size:13px;line-height:21px;color:#f2f2f2;text-align:center}
.btn-outline{left:544px;top:409px;width:140px;height:38px;border:2px solid var(--white);color:var(--white);font-size:12px;font-weight:700;display:flex;align-items:center;justify-content:center}

/* advantages */
.advantages{top:694px;height:630px;background:var(--white)}
.advantages .section-title{top:76px}
.advantages .title-rule{top:119px}
.advantages .intro{top:145px;left:200px;width:800px;text-align:center;font-size:13px;line-height:23px;color:#5a2020}
.adv-graphic{left:0;top:0}
.adv-item h3{font-size:13px;font-weight:700;color:var(--ink);line-height:16px}
.adv-item p{font-size:11.5px;line-height:15px;color:var(--muted);margin-top:6px}
.adv-item.right{text-align:right}

/* solutions */
.solutions{top:1324px;height:592px;background:linear-gradient(180deg,#f7f7f7,#e8e8e8)}
.solutions .section-title{top:93px}
.solutions .title-rule{top:136px}
.solutions .intro{top:156px;font-size:15.5px;color:#555}
.sol-card{top:275px;width:227px;height:192px;border:2px solid var(--line);text-align:center}
.sol-card .icon{position:absolute;left:72px;top:-38px;width:83px;height:74px;background:var(--white);border:2px solid #d02025;padding:3px}
.sol-card .icon div{width:100%;height:100%;background:linear-gradient(135deg,#4a0204,#c00a10);display:flex;align-items:center;justify-content:center}
.sol-card h3{position:absolute;top:59px;left:0;width:100%;font-size:14px;font-weight:600;color:var(--ink);letter-spacing:.5px}
.sol-card p{position:absolute;top:82px;left:20px;width:187px;font-size:11px;line-height:16px;color:#666}
.btn-pill{position:absolute;top:137px;left:60px;width:106px;height:29px;border:2px solid var(--red);border-radius:15px;color:var(--red);font-size:9.5px;font-weight:700;display:flex;align-items:center;justify-content:center}

/* help */
.help{top:1916px;height:550px;background:
  radial-gradient(ellipse at 80% 40%,#d00c12 0%,transparent 60%),
  linear-gradient(90deg,#3a0203 0%,#7a0507 35%,#b8080e 70%,#d50b12 100%)}
.help-photo{left:0;top:0;width:1200px;height:550px}
.help h2{left:133px;top:135px;font-size:30px;font-weight:700;color:var(--white);letter-spacing:.5px}
.help p{left:131px;top:203px;width:400px;font-size:13.5px;line-height:23px;color:#f4f4f4}
.btn-solid{left:131px;top:351px;width:151px;height:40px;border-radius:20px;background:var(--red);color:var(--white);font-size:14px;font-weight:600;display:flex;align-items:center;justify-content:center}
.app-window{left:603px;top:77px;width:473px;height:351px;background:#fff;border-radius:4px;overflow:hidden;box-shadow:0 6px 24px rgba(0,0,0,.35)}
.app-window .bar{height:16px;background:#e4e4e4;display:flex;gap:5px;align-items:center;padding-left:10px}
.app-window .bar i{width:7px;height:7px;border-radius:50%;background:#9a9a9a;display:block}
.app-window .screen{position:absolute;top:16px;left:0;width:473px;height:335px;background:linear-gradient(180deg,#f3f3f3 0%,#e9eef3 40%,#f5f5f5 100%)}

/* testimonials */
.testimonials{top:2466px;height:574px;background:var(--white)}
.testimonials .section-title{top:97px}
.testimonials .title-rule{top:138px}
.quote-frame{left:280px;top:202px;width:641px;height:243px;border:2px solid #e1262c}
.quote-card{left:267px;top:190px;width:642px;height:244px;background:linear-gradient(90deg,#c1070d,#e30b12)}
.client-name{left:325px;top:284px;font-size:24px;font-weight:600;color:var(--white);display:flex;align-items:center;gap:8px}
.client-name i{width:14px;height:14px;border-radius:50%;border:2px solid var(--white);display:block}
.quote-divider{left:445px;top:231px;width:1px;height:180px;background:rgba(255,255,255,.7)}
.quote-text{left:491px;top:244px;width:400px;font-size:14px;font-style:italic;line-height:22px;color:var(--white)}
.avatar{left:486px;top:343px;width:42px;height:42px;border-radius:50%;background:linear-gradient(135deg,#d9c2b0,#8a6a58);border:2px solid #f0f0f0}
.author{left:544px;top:345px;color:var(--white)}
.author strong{display:block;font-size:13px;font-weight:700}
.author span{display:block;font-size:11px;margin-top:6px}
.nav-arrow{width:40px;height:40px;top:2761px}

/* quote */
.request{top:3040px;height:428px;background:
  radial-gradient(ellipse at 20% 30%,#9a0508 0%,transparent 55%),
  linear-gradient(90deg,#6a0305 0%,#b0070c 45%,#e00a12 100%)}
.request h2{top:67px;font-size:29px;font-weight:700;color:var(--white);letter-spacing:.5px}
.request .rule{left:555px;top:113px;width:90px;height:3px;background:var(--white)}
.field{background:var(--white);font-size:13px;color:#666;padding:13px 16px;border:1px solid #ddd}
.submit{left:534px;top:309px;width:151px;height:43px;border-radius:22px;background:var(--red);color:var(--white);font-size:16px;font-weight:700;display:flex;align-items:center;justify-content:center}

/* footer */
.site-footer{top:3468px;height:329px;background:var(--footer)}
.site-footer .logo{left:153px;top:73px;font-size:44px;color:var(--red)}
.social{left:156px;top:141px;display:flex;gap:6px}
.social i{width:22px;height:22px;border-radius:50%;background:var(--white);display:block}
.legal{left:155px;top:183px;font-size:11px;line-height:23px;color:#b5b5b5}
.col-divider{top:0;width:1px;height:329px;background:#333}
.col-mark{width:2px;height:20px;background:var(--red);top:88px}
.footer-col h4{font-size:14px;font-weight:600;color:var(--white);letter-spacing:.5px}
.footer-col ul{list-style:none;margin-top:18px}
.footer-col li{font-size:11.5px;color:#aaa;line-height:24.5px}
</style>
</head>
<body>

<header class="site-header">
  <div class="abs logo brand">VexaQuor<sup>®</sup></div>
  <nav class="main-nav">
    <a class="active" style="left:402px">ABOUT US</a>
    <a style="left:519px">SERVICES</a>
    <a style="left:622px">FEATURES</a>
    <a style="left:728px">WHY</a>
    <a style="left:806px">METHADOLOGY</a>
    <a style="left:951px">CONTACT</a>
  </nav>
</header>

<section class="hero">
  <div class="abs hero-photo" role="img" aria-label="Offshore drilling platform at dusk under a stormy red sky with lightning"></div>
  <div class="abs center brand">VexaQuor<sup>®</sup></div>
  <h1 class="abs center">RISK ANALYSIS SOFTWARE<br>FOR THE PETROLEUM PROFESSIONAL</h1>
  <p class="abs">VexaQuor® offers the petroleum industry a powerful, yet easy-to-use, well cost and scheduling risk analysis software. Our unique and intuitive user interface is designed specifically for the petroleum professional and offers an efficient and consistent way to create an accurate risked drilling and completion AFE.</p>
  <div class="abs btn-outline">LEARN MORE</div>
</section>

<section class="advantages">
  <h2 class="abs center section-title">VEXAQUOR <span>ADVANTAGES</span></h2>
  <div class="abs title-rule"></div>
  <p class="abs intro">VexaQuor® enables E&amp;P Companies to thoroughly analyze and better manage risk, deliver more accurate cost estimates, reduce NPT, and avoid costly drilling problems. VexaQuor® enlightens E&amp;P managers by providing quick and clear insight into the statistical parameters that compiled each cost estimate.</p>

  <svg class="abs adv-graphic" width="1200" height="630" viewBox="0 0 1200 630">
    <defs>
      <radialGradient id="core" cx="50%" cy="40%" r="60%">
        <stop offset="0" stop-color="#e0141b"/><stop offset="1" stop-color="#7a0407"/>
      </radialGradient>
      <filter id="soft" x="-30%" y="-30%" width="160%" height="160%"><feDropShadow dx="0" dy="2" stdDeviation="5" flood-color="#000" flood-opacity=".12"/></filter>
    </defs>
    <path d="M425 494 A188 188 0 0 1 786 487" fill="none" stroke="#dcdcdc" stroke-width="3"/>
    <circle cx="607" cy="515" r="167" fill="url(#core)"/>
    <g fill="#fff" stroke="#c8151b" stroke-width="4">
      <circle cx="497" cy="381" r="6"/><circle cx="702" cy="373" r="6"/>
      <circle cx="425" cy="494" r="6"/><circle cx="786" cy="487" r="6"/>
    </g>
    <g fill="#fff" filter="url(#soft)">
      <circle cx="454" cy="326" r="44"/><circle cx="747" cy="323" r="44"/>
      <circle cx="363" cy="488" r="44"/><circle cx="858" cy="479" r="44"/>
    </g>
    <g fill="none" stroke="#d0151b" stroke-width="2" stroke-linecap="round" stroke-linejoin="round">
      <path d="M440 342v-12M447 342v-18M454 342v-10M461 342v-16M468 342v-8M437 344h34M440 312l10 10 8-6 12 14"/>
      <circle cx="745" cy="321" r="13"/><circle cx="745" cy="321" r="6"/><path d="M755 331l9 9"/>
      <circle cx="363" cy="478" r="12"/><path d="M363 471v14M359 474h7M359 482h7M345 498l10-4 12 4 12-8"/>
      <path d="M858 463l16 28h-32z"/><path d="M858 473v9M858 486v1"/>
    </g>
    <text x="607" y="528" text-anchor="middle" font-family="Montserrat, Arial, sans-serif" font-weight="800" font-size="48" fill="#fff" letter-spacing="-1">VexaQuor®</text>
  </svg>

  <div class="abs adv-item right" style="right:806px;top:306px;width:200px">
    <h3>Reduce NPT</h3><p>Lorem ipsum dolor sit amet,<br>consectetur adipiscing.</p>
  </div>
  <div class="abs adv-item" style="left:801px;top:296px;width:200px">
    <h3>Optimize Operations</h3><p>Lorem ipsum dolor sit amet,<br>consectetur adipiscing.</p>
  </div>
  <div class="abs adv-item right" style="right:898px;top:460px;width:160px">
    <h3>Accurate Cost<br>Estimates</h3><p>Lorem ipsum dolor sit<br>amet, consectetur ad-<br>ipiscing.</p>
  </div>
  <div class="abs adv-item" style="left:911px;top:456px;width:150px">
    <h3>Risk-Empowered!</h3><p>Lorem ipsum dolor sit<br>amet, consectetur<br>adipiscing.</p>
  </div>
</section>

<section class="solutions">
  <h2 class="abs center section-title">VEXAQUOR <span>SOLUTIONS</span></h2>
  <div class="abs title-rule"></div>
  <p class="abs center intro">VexaQuor® – a leading edge, breakthrough software solution for well project risk analysis.</p>

  <div class="abs sol-card" style="left:136px">
    <div class="icon"><div><svg width="34" height="30" fill="none" stroke="#fff" stroke-width="2"><path d="M4 28V18M11 28V12M18 28V15M25 28V8M2 29h30M4 12l8-6 7 4 10-8"/></svg></div></div>
    <h3>CONSISTENT</h3><p>Lorem ipsum dolor sit amet, consectetur adipiscing elitsed</p><div class="btn-pill">LEARN MORE</div>
  </div>
  <div class="abs sol-card" style="left:374px">
    <div class="icon"><div><svg width="34" height="34" fill="none" stroke="#fff" stroke-width="2"><circle cx="17" cy="19" r="12"/><path d="M17 19l5-5M14 3h6M17 3v4"/></svg></div></div>
    <h3>QUICK</h3><p>Lorem ipsum dolor sit amet, consectetur adipiscing elitsed</p><div class="btn-pill">LEARN MORE</div>
  </div>
  <div class="abs sol-card" style="left:614px">
    <div class="icon"><div><svg width="30" height="36" fill="none" stroke="#fff" stroke-width="2"><path d="M12 20V6a3 3 0 0 1 6 0v12l6 1c3 1 4 3 3 6l-2 9H12l-6-9c-1-2 1-4 3-3l3 3"/></svg></div></div>
    <h3>EASY TO USE</h3><p>Lorem ipsum dolor sit amet, consectetur adipiscing elitsed</p><div class="btn-pill">LEARN MORE</div>
  </div>
  <div class="abs sol-card" style="left:850px">
    <div class="icon"><div><svg width="36" height="30" fill="none" stroke="#fff" stroke-width="2"><rect x="2" y="2" width="32" height="26" rx="2"/><path d="M2 8h32M8 16h14M8 22h14"/><circle cx="27" cy="19" r="3"/></svg></div></div>
    <h3>GAIN CONTROL</h3><p>Lorem ipsum dolor sit amet, consectetur adipiscing elitsed</p><div class="btn-pill">LEARN MORE</div>
  </div>
</section>

<section class="help">
  <div class="abs help-photo" role="img" aria-label="Refinery silhouette fading into a deep red background"></div>
  <svg class="abs" style="left:530px;top:220px" width="160" height="160"><circle cx="80" cy="80" r="70" fill="none" stroke="rgba(255,255,255,.25)" stroke-width="2"/><circle cx="80" cy="80" r="52" fill="none" stroke="rgba(255,255,255,.18)" stroke-width="2"/></svg>
  <h2 class="abs">HOW CAN IT HELP?</h2>
  <p class="abs">Lorem ipsum dolor sit amet, consectetur adipiscing elit, sed do eiusmod tempor incididunt ut labore et dolore magna aliqua. Ut enim ad minim veniam, quis nostrud exercitation ullamco laboris nisi ut aliquip ex ea commodo consequat. Duis aute irure dolor in</p>
  <div class="abs btn-solid">LEARN MORE</div>
  <div class="abs app-window">
    <div class="bar"><i></i><i></i><i></i></div>
    <div class="screen" role="img" aria-label="Screenshot of the VexaQuor application showing a drilling cost estimate table"></div>
  </div>
</section>

<section class="testimonials">
  <h2 class="abs center section-title">WHAT OUR CLIENT SAYS</h2>
  <div class="abs title-rule"></div>
  <div class="abs quote-frame"></div>
  <div class="abs quote-card"></div>
  <div class="abs client-name"><i></i>Norvane</div>
  <div class="abs quote-divider"></div>
  <p class="abs quote-text">"Lorem ipsum dolor sit amet, consectetur adipiscing elit, sed do eiusmod tempor incididunt ut labore et dolore magna aliqua. Ut enim ad minim veniam, quis nostrud exercitation ullamco laboris nisi ut aliquip ex</p>
  <div class="abs avatar" role="img" aria-label="Portrait of the client"></div>
  <div class="abs author"><strong>Daren Holt</strong><span>Company CEO Founder</span></div>
  <svg class="abs" style="left:833px;top:362px" width="38" height="26" fill="rgba(255,255,255,.8)"><path d="M0 26V12L8 0h6L9 12h6v14zM22 26V12L30 0h6l-5 12h6v14z"/></svg>
</section>
<svg class="abs nav-arrow" style="left:162px" viewBox="0 0 40 40"><circle cx="20" cy="20" r="18.5" fill="none" stroke="#777" stroke-width="2"/><path d="M23 12l-8 8 8 8" fill="none" stroke="#555" stroke-width="2.5"/></svg>
<svg class="abs nav-arrow" style="left:1003px" viewBox="0 0 40 40"><circle cx="20" cy="20" r="18.5" fill="none" stroke="#e30613" stroke-width="2"/><path d="M17 12l8 8-8 8" fill="none" stroke="#e30613" stroke-width="2.5"/></svg>

<section class="request">
  <div class="abs" style="inset:0" role="img" aria-label="Abstract network of connected points over a red background"></div>
  <h2 class="abs center">REQUEST A QUOTE</h2>
  <div class="abs rule"></div>
  <div class="abs field" style="left:237px;top:141px;width:370px;height:41px">Name</div>
  <div class="abs field" style="left:237px;top:191px;width:370px;height:41px">Email address</div>
  <div class="abs field" style="left:237px;top:241px;width:370px;height:42px">Phone</div>
  <div class="abs field" style="left:615px;top:141px;width:371px;height:142px">Message</div>
  <div class="abs submit">Submit</div>
</section>

<footer class="site-footer">
  <div class="abs logo brand">VexaQuor<sup>®</sup></div>
  <div class="abs social" aria-label="Social links"><i></i><i></i><i></i></div>
  <div class="abs legal">VexaQuor® Registered Trademark 2021<br>All Rights Reserved</div>
  <div class="abs col-divider" style="left:445px"></div>
  <div class="abs col-divider" style="left:684px"></div>
  <div class="abs col-divider" style="left:909px"></div>
  <div class="abs col-mark" style="left:445px"></div>
  <div class="abs col-mark" style="left:684px"></div>
  <div class="abs col-mark" style="left:909px"></div>
  <div class="abs footer-col" style="left:469px;top:85px"><h4>COMPANY</h4><ul><li>About VexaQuor</li><li>Why we are</li><li>What we do</li><li>Features</li></ul></div>
  <div class="abs footer-col" style="left:709px;top:85px"><h4>RESOURCES</h4><ul><li>Our Values</li><li>Press</li><li>Careers</li><li>Support</li></ul></div>
  <div class="abs footer-col" style="left:933px;top:85px"><h4>CONTACT US</h4><ul style="line-height:17px"><li style="line-height:17px">Call us now<br>555-014-2290</li><li style="line-height:17px;margin-top:14px">Email address<br>info@vexaquor-demo.net</li></ul></div>
</footer>

</body>
</html>
```